KELVARO Website - Innovative Products need a creative designer!

I require a bold, fun and interactive website designing for my company rebrand. I am in the process of having new logo's designed but the colour scheme is already established.

Colours: Yellow (PRIMARY) : #C6FF02 / RGB: 198, 255, 2 Black (SECONDARY): #000000 / RGB: 0, 0, 0

The company specialises in Temporary Modular Space, so i would like to see creative blocks illustrating the products. (Products listed below). Please only design the homepage and the winner will then design / code the full thing. Please include an area that elaborates on the sustainablity factor of the company. I like animated emblems, pictures and writing. There will be on going work on this, as I will need the designer to provide up keep and maintenance on it as we progress.

Menu Pages:

The Solutions - (Products):
Tradecrate: An innovative point of sale units specifically designed for the sale of Merchandise. It transports like a normal shipping container, but once situated expands outwards to increase the internal footprint by up to 90%. And once in situ are completely antivandal, removing the requirement for multiple security personnel and protecting your products. It also provide sales points to a 180 degree angle, maximising revenue and reducing queue time. - Completely customisable.

Loftcase: A penthouse in a box, the innovative nature of the unit enables it to be situated anywhere. Ideal for glamping sites, guest houses at private properties for temporary Festival accommodation. The unit comes fully furnished with a kitchenette, en suite bathroom and ample space for a double bed and a living area. This is truly the luxurious and affordable option for temporary accommodation.

Glasspod: A standalone product, but also an accessory to the Tradecrate. A flat pack system that is truly 100% modular, all wall panels can be installed tailored to your requirements. This can be an on site office, or a glass display box for brand activations. Installed on the ground or on the roof of the Tradecrate, it is a flexible piece of equipment designed that is not only premium but affordable. - Completely customisable.

RTRange:
RT14: A quick install and sustainable design for use on a variety of sites. The cabins collapse down enabling multiple units to be transported on a 1no. truck. We can transport 20no. units on 1no. 40ft truck, reducing the carbon footprint of events drastically. When erected, they can be stacked to create 2no. floors. - Completely customisable.
RT28: Same as the above but a 20ft cabin. These can transport 10no. units on a 40ft trailer. Can be stacked to create 2no. floors. - Completely customisable.

The Industries:
Merchandise & Shows
Sports & Stadia
Brand Activations
Retail & Stores
Events & Festivals
Automotive
Exhibitions

The Company: Will confirm all information once the winner is selected.

Contact: Will confirm all information once the winner is selected.

Events, Merchandise, Stadiums, Automotive, Brand Activations, Commercial

Coded - Design and coding required

5+ page

Designer to choose colors to be used in the design.

• Interactive elements, engaging design, innovative movements, be bright and bold. But most importantly be informative and easy to navigate.
• Animations of blocks, moving emblems.
• No pre existing templates

```html
<!DOCTYPE html>
<html lang="en">
<head>
<meta charset="utf-8">
<title>KELVARO — Temporary Modular Space Experts</title>
<link href="https://fonts.googleapis.com/css2?family=Russo+One&family=Montserrat:wght@400;500;600;700&display=swap" rel="stylesheet">
<style>
:root{
  --lime:#C6FF02;
  --black:#000;
  --ink:#1a1a1a;
  --dark:#1c1c1c;
  --paper:#f3f1f2;
  --white:#fff;
  --grey:#444;
  --light:#e6e6e6;
}
*{margin:0;padding:0;box-sizing:border-box}
html,body{width:1200px;height:4608px;overflow:hidden}
body{position:relative;font-family:"Montserrat",sans-serif;color:var(--ink);background:var(--white)}
.abs{position:absolute}
.display{font-family:"Russo One",sans-serif;text-transform:uppercase;letter-spacing:1px}

/* header */
.hero{left:0;top:0;width:1200px;height:556px;background:radial-gradient(ellipse at 50% 70%,#5a5a5a 0%,#2a2a2a 40%,#0d0d0d 80%)}
.brand-tab{left:0;top:0;width:366px;height:68px;background:var(--lime);clip-path:polygon(0 0,100% 0,88% 100%,0 100%);display:flex;align-items:center;padding-left:110px;gap:14px}
.brand-tab .mark{width:30px;height:30px;background:var(--black)}
.brand-tab .name{font-family:"Russo One",sans-serif;font-size:30px;color:var(--black)}
.nav{left:415px;top:26px;display:flex;gap:28px;font-size:15px;font-weight:500;color:var(--white)}
.quote{left:939px;top:14px;width:148px;height:43px;background:var(--lime);color:var(--black);font-weight:700;font-size:15px;display:flex;align-items:center;justify-content:center;clip-path:polygon(6% 0,100% 0,94% 100%,0 100%)}
.hero-title{left:0;top:160px;width:1200px;text-align:center;font-size:46px;line-height:63px;color:var(--lime)}
.hero-rule{left:563px;top:294px;width:74px;height:3px;background:var(--lime)}

/* section headings */
.sec-title{left:0;width:1200px;text-align:center;font-size:44px;color:var(--ink)}
.divider{left:510px;width:180px;height:30px;display:flex;align-items:center;justify-content:space-between}
.divider i{display:block;width:58px;height:2px;background:var(--lime)}
.divider b{display:block;width:22px;height:22px;border:3px solid var(--ink);transform:rotate(45deg)}
.on-dark .divider b{border-color:var(--white)}
.on-dark .sec-title{color:var(--white)}

/* solutions */
.solutions{left:0;top:556px;width:1200px;height:1935px;background:var(--paper)}
.hex-photo{clip-path:polygon(50% 0,100% 25%,100% 75%,50% 100%,0 75%,0 25%)}
.band{height:57px;background:var(--lime);display:flex;align-items:center;font-size:32px;color:var(--ink)}
.copy{font-size:14.6px;line-height:28.4px;color:var(--grey)}
.copy strong{font-weight:700;color:var(--ink)}
.justify{text-align:justify}

/* series */
.series{left:0;top:2491px;width:1200px;height:894px;background:var(--dark)}
.slide{left:177px;top:234px;width:846px;height:377px;background:linear-gradient(180deg,#9cb7d6 0%,#cfdbe8 42%,#d9d9d9 55%,#b9b9b6 75%,#6f8a4c 90%,#557034 100%)}
.slide-corner{left:974px;top:225px;width:58px;height:55px;background:var(--lime);clip-path:polygon(0 0,100% 0,100% 100%)}
.slide-label{left:483px;top:581px;width:234px;height:66px;background:var(--lime);display:flex;align-items:center;justify-content:center;font-size:32px;color:var(--ink)}
.arrow{top:431px;width:34px;height:24px}
.series-copy{left:170px;top:697px;width:860px;text-align:center;font-size:14.6px;line-height:28.4px;color:var(--light)}
.series-copy strong{color:var(--white)}

/* industries */
.industries{left:0;top:3385px;width:1200px;height:924px;background:var(--white)}
.ind{width:220px;text-align:center}
.ind .hex{width:146px;height:168px;margin:0 auto;background:var(--lime);clip-path:polygon(50% 0,100% 25%,100% 75%,50% 100%,0 75%,0 25%);display:flex;align-items:center;justify-content:center}
.ind .hex svg{width:82px;height:82px;fill:none;stroke:var(--black);stroke-width:3;stroke-linejoin:round;stroke-linecap:round}
.ind p{margin-top:38px;font-size:19px;line-height:27px;color:#333;letter-spacing:.5px}

/* footer */
.footer{left:0;top:4309px;width:1200px;height:299px;background:var(--dark)}
.foot-brand{left:0;top:75px;width:1200px;display:flex;justify-content:center;align-items:center;gap:20px}
.foot-brand .mark{width:44px;height:44px;background:var(--lime)}
.foot-brand .name{font-family:"Russo One",sans-serif;font-size:50px;color:var(--lime)}
.foot-nav{left:0;top:180px;width:1200px;display:flex;justify-content:center;gap:28px;font-size:15px;color:var(--white)}
.legal{left:0;top:222px;width:1200px;text-align:center;font-size:15px;color:var(--white)}
</style>
</head>
<body>

<header class="abs hero" role="img" aria-label="Photo of a black sports car displayed inside a glass modular showroom at night">
</header>
<div class="abs brand-tab"><span class="mark"></span><span class="name">KELVARO</span></div>
<nav class="abs nav"><span>Home</span><span>The Solutions</span><span>RT Range</span><span>The Industries</span><span>Contact</span></nav>
<div class="abs quote">Request Quote</div>
<h1 class="abs hero-title display">Temporary Modular<br>Space Experts</h1>
<div class="abs hero-rule"></div>

<section class="abs solutions">
  <h2 class="abs sec-title display" style="top:76px">The Solutions</h2>
  <div class="abs divider" style="top:146px"><i></i><b></b><i></i></div>

  <div class="abs hex-photo" style="left:111px;top:249px;width:416px;height:509px;background:linear-gradient(180deg,#b9bec4 0%,#7c8288 35%,#2b2b2b 55%,#3a3a3a 100%)" role="img" aria-label="Photo of an expanded merchandise trading container with lime branding"></div>
  <div class="abs band display" style="left:429px;top:315px;width:352px;padding-left:139px">Tradecrate</div>
  <p class="abs copy" style="left:569px;top:399px;width:522px">An innovative point of sale units specifically designed for the sale of Merchandise. It transports like a normal shipping container, but once situated expands outwards to increase the internal footprint by up to 90%. And once in situ are completely antivandal, removing the requirement for multiple security personnel and protecting your products. It also provide sales points to a 180 degree angle, maximising revenue and reducing queue time.<br><strong>- Completely customisable.</strong></p>

  <div class="abs band display" style="left:409px;top:837px;width:360px;padding-left:34px;clip-path:polygon(0 0,100% 0,100% 100%,0 100%)">Loftcase</div>
  <p class="abs copy justify" style="left:113px;top:921px;width:522px">A penthouse in a box, the innovative nature of the unit enables it to be situated anywhere. Ideal for glamping sites, guest houses at private properties for temporary Festival accommodation. The unit comes fully furnished with a kitchenette, en suite bathroom and ample space for a double bed and a living area. This is truly the luxurious and affordable option for temporary accommodation.</p>
  <div class="abs hex-photo" style="left:672px;top:776px;width:419px;height:510px;background:linear-gradient(180deg,#eef1f3 0%,#8a9a78 30%,#2a2e33 55%,#1e2226 75%,#8a6a50 100%)" role="img" aria-label="Photo of a black accommodation cabin with glass doors among trees"></div>

  <div class="abs hex-photo" style="left:111px;top:1295px;width:416px;height:509px;background:linear-gradient(180deg,#9fbde0 0%,#c8d5e2 30%,#d3d6da 55%,#9ea3a8 85%,#6c7074 100%)" role="img" aria-label="Photo of a two storey white modular unit with glass upper level"></div>
  <div class="abs band display" style="left:429px;top:1357px;width:352px;padding-left:139px">Glasspod</div>
  <p class="abs copy" style="left:569px;top:1444px;width:522px">A standalone product, but also an accessory to the Tradecrate. A flat pack system that is truly 100% modular, all wall panels can be installed tailored to your requirements. This can be an on site office, or a glass display box for brand activations. Installed on the ground or on the roof of the Tradecrate, it is a flexible piece of equipment designed that is not only premium but affordable.<br><strong>- Completely customisable.</strong></p>
</section>

<section class="abs series on-dark">
  <h2 class="abs sec-title display" style="top:92px">RT Range</h2>
  <div class="abs divider" style="top:162px"><i></i><b></b><i></i></div>
  <svg class="abs arrow" style="left:34px" viewBox="0 0 34 24" fill="none" stroke="#fff" stroke-width="2.4"><path d="M32 12H3M13 2L3 12l10 10"/></svg>
  <div class="abs slide" role="img" aria-label="Photo of stacked white modular cabins at an outdoor event site"></div>
  <div class="abs slide-corner"></div>
  <svg class="abs arrow" style="left:1122px" viewBox="0 0 34 24" fill="none" stroke="#fff" stroke-width="2.4"><path d="M2 12h29M21 2l10 10-10 10"/></svg>
  <div class="abs slide-label display">RT14</div>
  <p class="abs series-copy">A quick install and sustainable design for use on a variety of sites. The cabins collapse down enabling multiple units to be transported on a 1no. truck. We can transport 20no. units on 1no. 40ft truck, reducing the carbon footprint of events drastically. When erected, they can be stacked to create 2no. floors.<br><strong>- Completely customisable.</strong></p>
</section>

<section class="abs industries">
  <h2 class="abs sec-title display" style="top:80px">The Industries</h2>
  <div class="abs divider" style="top:148px"><i></i><b></b><i></i></div>

  <div class="abs ind" style="left:114px;top:289px">
    <div class="hex"><svg viewBox="0 0 80 80"><path d="M14 20h52l-18 18-8-6-8 6z"/><path d="M32 38L20 62M48 38l12 24M20 62l6 4M60 62l-6 4"/></svg></div>
    <p>MERCHANDISE &amp;<br>SHOWS</p>
  </div>
  <div class="abs ind" style="left:364px;top:289px">
    <div class="hex"><svg viewBox="0 0 80 80"><circle cx="36" cy="34" r="20"/><path d="M16 34h40M36 14v40M22 20c8 8 8 20 0 28M50 20c-8 8-8 20 0 28"/><ellipse cx="54" cy="56" rx="14" ry="9"/><path d="M46 56h16M50 53v6M54 53v6M58 53v6"/></svg></div>
    <p>SPORTS &amp; STADIA</p>
  </div>
  <div class="abs ind" style="left:620px;top:289px">
    <div class="hex"><svg viewBox="0 0 80 80"><path d="M12 34h10l30-16v44L22 46H12z"/><path d="M22 46l4 16h8l-4-16"/><path d="M60 30c4 4 4 16 0 20M66 24c7 8 7 24 0 32"/><path d="M37 30l2 5 5 .5-4 3.5 1 5-4-3-4 3 1-5-4-3.5 5-.5z"/></svg></div>
    <p>BRAND<br>ACTIVATIONS</p>
  </div>
  <div class="abs ind" style="left:866px;top:289px">
    <div class="hex"><svg viewBox="0 0 80 80"><path d="M14 16h52v8H14z"/><path d="M14 24c0 6 9 6 9 0 0 6 8 6 8 0 0 6 9 6 9 0 0 6 8 6 8 0 0 6 9 6 9 0 0 6 9 6 9 0"/><path d="M18 32v34h44V32"/><path d="M24 44h14v22H24zM44 44h12v10H44z"/><path d="M12 66h56"/></svg></div>
    <p>RETAIL &amp; STORES</p>
  </div>

  <div class="abs ind" style="left:239px;top:571px">
    <div class="hex"><svg viewBox="0 0 80 80"><path d="M12 22l48-10M12 22l6 12 6-10 6 10 6-12 6 10 6-12"/><path d="M22 50l46 0M22 50l6 12 6-12 6 12 6-12 6 12 6-12"/><path d="M60 30l2 2M64 26l-2 2M16 56l2 2M14 62l2-2"/></svg></div>
    <p>EVENTS &amp;<br>FESTIVALS</p>
  </div>
  <div class="abs ind" style="left:489px;top:571px">
    <div class="hex"><svg viewBox="0 0 80 80"><path d="M40 10l3 7 7 .5-5.5 4.5 2 7-6.5-4-6.5 4 2-7-5.5-4.5 7-.5z"/><path d="M30 40h20v10l-4 16H34l-4-16z"/><path d="M34 40v-6M40 40v-8M46 40v-6"/><circle cx="18" cy="30" r="2"/><circle cx="62" cy="30" r="2"/><circle cx="16" cy="48" r="2"/><circle cx="64" cy="48" r="2"/></svg></div>
    <p>AUTOMOTIVE</p>
  </div>
  <div class="abs ind" style="left:741px;top:571px">
    <div class="hex"><svg viewBox="0 0 80 80"><path d="M14 14h52v36H14z"/><path d="M20 20h40v24H20z"/><path d="M22 42l10-10 8 8 6-6 12 10"/><circle cx="50" cy="27" r="3"/><path d="M22 50v16M58 50v16M30 50c0 10-8 10-8 16M50 50c0 10 8 10 8 16"/></svg></div>
    <p>EXHIBITIONS</p>
  </div>
</section>

<footer class="abs footer">
  <div class="abs foot-brand"><span class="mark"></span><span class="name">KELVARO</span></div>
  <nav class="abs foot-nav"><span>Home</span><span>The Solutions</span><span>RT Range</span><span>The Industries</span><span>Contact</span></nav>
  <p class="abs legal">2024 Kelvaro. All Rights Reserved.</p>
</footer>

</body>
</html>
```